earthmoving and roadworks company looking for a fresh and updated logo to help us stand out

We are looking for a business card design for our earthmoving, demolition and road works company named Wandermere Plant. We cover a broad range of work so our business card needs to be flexible to suit all of the different services we provide. We have a few different bits of machinery including several water trucks for transporting water and spraying the roads, an excavator (digger) for earthmoving, a tipper truck that carries grain/soil and other items, a bobcat and two rollers. our business card needs to be simple but effective and bold. Our colour palette is yellow, black and white and I have attached a copy of our logo but please note our logo is only the 'Wandermere plant' bit with attached circle, the 'watercarts, rollers, cartage' below are not part of the logo. Please feel free to modify the logo to better suit the business card. The design must be easy to read and to the point. It should make us look reliable and professional.

Target Market(s)

Wide range of clients including government sectors and private individuals

Industry/Entity Type

Construction

Contact Information for Business Card

We need a business card that is bold and straight to the point but with easy to read information and an eye catching design. We are open to either a single sided or double sided design

Colors
fbee3d
fcf5b5
fbf289
fbed22

Requirements
Must have
• The business card must include
• our logo
• our contact details as listed below:
• Trevor Okafor
• Managing Director
• 02 6140 9375
• 0471 903 216
• wandermereplant@fernmail.example
Nice to have
• Nice to have a picture of machinery or part of machinery in the business card design. We would also like to incorporate our business activities which are: demolition, earthmoving, road works and cartage. It would also be highly desirable if it included a list of our machinery: Watercarts, Rollers, Excavator, Bobcat, Truck & Dog. we are open to the possibility of either single sided or double sided designs
Should not have
• should not have too many colours or detract from the main information. should not be too busy.

```html
<!DOCTYPE html>
<html lang="en">
<head>
<meta charset="utf-8">
<title>Wandermere Plant — Business Card</title>
<link rel="stylesheet" href="https://fonts.googleapis.com/css2?family=Open+Sans:wght@400;600;700&display=swap">
<style>
  :root {
    --backdrop: #3a3430;
    --card: #1c1c1c;
    --yellow: #fbed22;
    --white: #f2f2f2;
    --muted: #d9d9d9;
  }
  * { box-sizing: border-box; margin: 0; padding: 0; }
  html, body {
    width: 1200px; height: 844px; overflow: hidden;
    background: var(--backdrop);
    font-family: "Open Sans", Arial, sans-serif;
  }
  .stage {
    position: relative; width: 1200px; height: 844px;
    display: flex; align-items: center; justify-content: center; gap: 48px;
  }
  .card {
    position: relative; width: 530px; height: 303px;
    background: var(--card);
    box-shadow: 0 10px 30px rgba(0,0,0,.45);
  }
  .brand {
    display: flex; align-items: center; gap: 12px;
    color: var(--yellow); font-weight: 700; letter-spacing: .02em;
  }
  .brand-dot {
    width: 22px; height: 22px; border-radius: 50%; background: var(--yellow);
  }
  .card-front .brand { position: absolute; left: 190px; top: 58px; font-size: 28px; }
  .contact {
    position: absolute; right: 36px; top: 120px;
    list-style: none; text-align: right; color: var(--white); font-size: 14px; line-height: 24px;
  }
  .contact li { display: flex; justify-content: flex-end; align-items: center; gap: 9px; }
  .contact svg { width: 12px; height: 12px; fill: var(--yellow); }
  .contact .email { margin-top: 18px; }
  .person { position: absolute; left: 36px; top: 190px; }
  .person-name { color: var(--yellow); font-size: 19px; font-weight: 700; }
  .person-role { color: var(--white); font-size: 14px; margin-top: 2px; }
  .services {
    position: absolute; left: 36px; bottom: 28px;
    color: var(--yellow); font-size: 15px; font-weight: 600;
  }
  .card-back .brand {
    position: absolute; left: 0; right: 0; top: 96px; justify-content: center; font-size: 34px;
  }
  .card-back .brand-dot { width: 26px; height: 26px; }
  .machinery {
    position: absolute; left: 0; right: 0; bottom: 70px; text-align: center;
    color: var(--yellow); font-size: 14px; font-weight: 600;
  }
  .sep { margin: 0 5px; }
</style>
</head>
<body>
<main class="stage">
  <section class="card card-front">
    <div class="brand"><span class="brand-dot"></span><span>Wandermere Plant</span></div>
    <ul class="contact">
      <li>02 6140 9375
        <svg viewBox="0 0 24 24" aria-hidden="true"><path d="M6.6 10.8a15 15 0 0 0 6.6 6.6l2.2-2.2a1 1 0 0 1 1-.25 11.4 11.4 0 0 0 3.6.57 1 1 0 0 1 1 1V20a1 1 0 0 1-1 1A17 17 0 0 1 3 4a1 1 0 0 1 1-1h3.5a1 1 0 0 1 1 1c0 1.25.2 2.45.57 3.57a1 1 0 0 1-.25 1z"/></svg></li>
      <li>0471 903 216
        <svg viewBox="0 0 24 24" aria-hidden="true"><path d="M7 1h10a2 2 0 0 1 2 2v18a2 2 0 0 1-2 2H7a2 2 0 0 1-2-2V3a2 2 0 0 1 2-2zm0 4v13h10V5z"/></svg></li>
      <li>wandermereplant@fernmail.example
        <svg viewBox="0 0 24 24" aria-hidden="true"><path d="M2 5h20v14H2zm2 2v.5l8 5 8-5V7z"/></svg></li>
    </ul>
    <div class="person">
      <p class="person-name">Trevor Okafor</p>
      <p class="person-role">Managing Director</p>
    </div>
    <p class="services">Demolition<span class="sep">•</span>Earthmoving<span class="sep">•</span>Road Works<span class="sep">•</span>Cartage</p>
  </section>

  <section class="card card-back">
    <div class="brand"><span class="brand-dot"></span><span>Wandermere Plant</span></div>
    <p class="machinery">Watercarts<span class="sep">•</span>Rollers<span class="sep">•</span>Excavator<span class="sep">•</span>Bobcat<span class="sep">•</span>Truck &amp; Dog</p>
  </section>
</main>
</body>
</html>
```